Web Design for an Online Dating Web Site

We need an uncoded web design for a new online dating web site called zMatchy.net. Simplicity and boldness are the key factors in the successful design.
Please look at the requirements document attached for details.
Updates
Dear all,
Please AVOID USING A PICTURE OF A HAPPY COUPLE ON THE HOME PAGE of the site. We highly want to move away from this space as it makes our web site just like another dating web site.
We like something simple with web 2.0 look and feel. The examples in the Requirements Document are exactly the design we are after.
Regards
Tarn
Industry/Entity Type
Dating
Look and feel
Each slider illustrates characteristics of the customer's brand and the style your logo design should communicate.

```html
<!DOCTYPE html>
<html lang="en">
<head>
<meta charset="utf-8">
<title>zMatchy.net — Home</title>
<link rel="stylesheet" href="https://fonts.googleapis.com/css2?family=Ubuntu:wght@400;500;700&family=Arimo:wght@400;700&display=swap">
<style>
:root{
  --pink:#e5157a;
  --pink-light:#f04a9a;
  --grey-text:#555;
  --nav-text:#555;
  --teal-dark:#146b7d;
  --teal:#2a9bb0;
  --teal-light:#3bbcc6;
  --green:#9cc11a;
  --green-light:#c8e35a;
  --footer-bg:#f4f4f4;
  --line:#ddd;
  --white:#fff;
}
*{box-sizing:border-box;margin:0;padding:0}
html,body{width:1200px;height:835px;overflow:hidden;background:var(--white);font-family:'Arimo',Arial,sans-serif}
.page{position:relative;width:1200px;height:835px}

/* header */
.site-header{position:absolute;top:0;left:0;width:1200px;height:89px;background:linear-gradient(#fff,#f6f3f5)}
.brand{position:absolute;left:144px;top:18px;display:flex;align-items:center;gap:10px;font-family:'Ubuntu',sans-serif;font-weight:700;font-size:44px;color:var(--pink);letter-spacing:-1px}
.brand-dot{width:16px;height:16px;border-radius:50%;background:var(--pink)}
.brand-sub{position:absolute;left:232px;top:66px;font-size:10px;color:#888;font-family:'Arimo',sans-serif}
.login-field{position:absolute;top:26px;width:199px;height:27px;border:1px solid #ccc;border-radius:5px;background:linear-gradient(#f4f4f4,#fff);font-size:12px;color:#888;padding:6px 11px}
.login-field.user{left:533px}
.login-field.pass{left:743px}
.btn-login{position:absolute;left:954px;top:26px;width:97px;height:26px;border-radius:5px;background:linear-gradient(var(--pink-light),var(--pink));box-shadow:2px 3px 3px rgba(0,0,0,.2);color:#fff;font:700 13px 'Ubuntu',sans-serif;text-align:center;line-height:26px}
.or-label{position:absolute;left:856px;top:62px;font-size:16px;color:#777}

/* nav */
.main-nav{position:absolute;top:89px;left:0;width:1200px;height:38px;background:linear-gradient(#f3eff2,#e9e4e8);border-top:1px solid #d8d3d7}
.nav-item{position:absolute;top:5px;height:26px;line-height:26px;font:500 15px 'Ubuntu',sans-serif;color:var(--nav-text);transform:translateX(-50%)}
.nav-item.current{left:176px;width:67px;text-align:center;border:1px solid #ccc;border-radius:5px;background:linear-gradient(#fff,#eee)}
.share-icon{position:absolute;top:3px;width:30px;height:30px;border-radius:4px;box-shadow:0 1px 2px rgba(0,0,0,.3)}
.btn-more{position:absolute;left:974px;top:5px;width:78px;height:25px;border-radius:5px;background:linear-gradient(var(--pink-light),var(--pink));color:#fff;font:400 12px 'Ubuntu',sans-serif;line-height:25px;padding-left:16px;box-shadow:2px 2px 3px rgba(0,0,0,.2)}
.btn-more svg{position:absolute;right:12px;top:7px}

/* hero */
.hero{position:absolute;top:127px;left:0;width:1200px;height:365px;background:linear-gradient(var(--teal) 0%,#2688a0 35%,var(--teal-dark) 50%,#2b9db0 72%,var(--teal-light) 100%);border-top:3px solid #5fbccb;border-bottom:3px solid #5fc6cf}
.hero-title{position:absolute;left:223px;top:62px;font:400 28px 'Ubuntu',sans-serif;color:#fff;text-shadow:1px 1px 2px rgba(0,0,0,.4)}
.hero-text{position:absolute;left:223px;top:108px;width:295px;font-size:12.5px;line-height:22.5px;color:#fff}
.btn-signup{position:absolute;left:225px;top:256px;width:183px;height:46px;border:2px solid #e6f58c;border-radius:9px;background:linear-gradient(var(--green-light),var(--green) 50%,#8cb010);color:#fff;font:500 24px 'Ubuntu',sans-serif;text-align:center;line-height:40px;text-shadow:1px 1px 1px rgba(0,0,0,.3)}
.slider-dots{position:absolute;left:282px;top:322px;display:flex;gap:6px}
.slider-dots span{width:21px;height:21px;border-radius:50%;background:#9fdcef}
.slider-dots span.active{background:#fff}
.video-card{position:absolute;left:625px;top:22px;width:379px;height:323px;border-radius:9px;background:#fff;overflow:hidden}
.video-backdrop{position:absolute;left:38px;top:36px;width:302px;height:280px;border-radius:50% 50% 45% 45%;background:radial-gradient(#f6f6f6,#ececec)}
.video-play{position:absolute;left:110px;top:90px}
.video-label{position:absolute;left:0;width:100%;top:258px;text-align:center;font:400 22px Arimo,sans-serif;color:#222;text-shadow:1px 1px 2px rgba(0,0,0,.35)}

/* welcome */
.welcome{position:absolute;top:523px;left:144px;width:912px}
.welcome h1{font:400 28px Arimo,sans-serif;color:var(--pink)}
.welcome p{margin:8px 0 0 4px;font-size:15px;line-height:19.5px;color:var(--grey-text)}

/* footer */
.site-footer{position:absolute;top:689px;left:0;width:1200px;height:146px;background:var(--footer-bg);box-shadow:inset 0 4px 4px -2px rgba(0,0,0,.12)}
.footer-brand{position:absolute;left:144px;top:34px;display:flex;align-items:center;gap:8px;font:700 36px 'Ubuntu',sans-serif;color:#999;letter-spacing:-1px}
.footer-brand i{width:13px;height:13px;border-radius:50%;background:#999}
.footer-share{position:absolute;top:43px;width:31px;height:31px;border-radius:3px;box-shadow:0 1px 2px rgba(0,0,0,.3)}
.footer-rule{position:absolute;left:143px;right:140px;top:107px;border-top:1px solid var(--line)}
.copyright{position:absolute;left:143px;top:114px;font-size:10.5px;color:#111}
.footer-nav{position:absolute;right:140px;top:114px;display:flex;gap:16px;font-size:10.5px;color:#111}
</style>
</head>
<body>
<div class="page">
  <header class="site-header">
    <div class="brand"><span>zMatchy</span><span class="brand-dot"></span></div>
    <div class="brand-sub">zmatchy.net</div>
    <div class="login-field user">Username</div>
    <div class="login-field pass">Password</div>
    <div class="btn-login">Login</div>
    <div class="or-label">OR</div>
  </header>

  <nav class="main-nav">
    <span class="nav-item current">Home</span>
    <span class="nav-item" style="left:262px">Why</span>
    <span class="nav-item" style="left:372px">How It Works</span>
    <span class="nav-item" style="left:494px">Sign Up</span>
    <span class="nav-item" style="left:600px">Our Blog</span>
    <span class="share-icon" role="img" aria-label="Share button" style="left:759px;background:#3b5a98"></span>
    <span class="share-icon" role="img" aria-label="Share button" style="left:804px;background:#d8d8d8"></span>
    <span class="share-icon" role="img" aria-label="Share button" style="left:849px;background:#6b1f6e"></span>
    <span class="share-icon" role="img" aria-label="Share button" style="left:893px;background:#e8e8e8"></span>
    <span class="share-icon" role="img" aria-label="Share button" style="left:936px;background:#1f5ca8"></span>
    <span class="btn-more">More
      <svg width="12" height="12" viewBox="0 0 12 12"><circle cx="6" cy="6" r="6" fill="#fff"/><path d="M6 3v6M3 6h6" stroke="#e5157a" stroke-width="2"/></svg>
    </span>
  </nav>

  <section class="hero">
    <h2 class="hero-title">Example Slider Page 1</h2>
    <p class="hero-text">Lorem ipsum dolor sit amet, consectetur adipiscing elit. Integer dictum, neque ut imperdiet pellentesque, nulla tellus tempus magna, sed consectetur orci metus a justo. Aliquam ac congue nunc. Mauris a tortor ut massa egestas tempus. Pellentesque tincidunt fermentum diam sagittis ullamcorper.</p>
    <div class="btn-signup">Sign Up</div>
    <div class="slider-dots"><span class="active"></span><span></span><span></span><span></span><span></span></div>
    <div class="video-card">
      <div class="video-backdrop" role="img" aria-label="Soft decorative background illustration"></div>
      <svg class="video-play" width="148" height="148" viewBox="0 0 148 148">
        <defs><linearGradient id="ring" x1="0" y1="0" x2="0" y2="1"><stop offset="0" stop-color="#35b9c8"/><stop offset="1" stop-color="#1c8aa6"/></linearGradient></defs>
        <circle cx="74" cy="74" r="73" fill="url(#ring)"/>
        <circle cx="74" cy="74" r="58" fill="#fff"/>
        <path d="M58 46 L102 74 L58 102 Z" fill="#2fb2c2"/>
      </svg>
      <div class="video-label">Watch a Video</div>
    </div>
  </section>

  <section class="welcome">
    <h1>Welcome to zMatchy</h1>
    <p>Lorem ipsum dolor sit amet consectetur. Lorem ipsum dolor sit amet consectetur. Lorem ipsum dolor sit amet consectetur. Lorem ipsum dolor sit amet consectetur. Lorem ipsum dolor sit amet consectetur. Lorem ipsum dolor sit amet consectetur. Lorem ipsum dolor sit amet consectetur. Lorem ipsum dolor sit amet consectetur. Lorem ipsum dolor sit amet consectetur. Lorem ipsum dolor sit amet consectetur. Lorem ipsum dolor sit amet consectetur. Lorem ipsum dolor sit amet consectetur. Lorem ipsum dolor sit amet consectetur. Lorem ipsum dolor sit amet consectetur. Lorem ipsum dolor sit amet consectetur.</p>
  </section>

  <footer class="site-footer">
    <div class="footer-brand"><span>zMatchy</span><i></i></div>
    <span class="footer-share" role="img" aria-label="Share button" style="left:793px;background:#3b5a98"></span>
    <span class="footer-share" role="img" aria-label="Share button" style="left:832px;background:#7fcbe6"></span>
    <span class="footer-share" role="img" aria-label="Share button" style="left:872px;background:#2a7fb0"></span>
    <span class="footer-share" role="img" aria-label="Share button" style="left:912px;background:#1f5ca8"></span>
    <span class="footer-share" role="img" aria-label="Share button" style="left:950px;background:#6b1f6e"></span>
    <span class="footer-share" role="img" aria-label="Share button" style="left:990px;background:#d8d8d8"></span>
    <span class="footer-share" role="img" aria-label="Share button" style="left:1030px;background:#cfd8e0"></span>
    <div class="footer-rule"></div>
    <div class="copyright">© 2011 zmatchy. All Rights Reserved</div>
    <nav class="footer-nav"><span>Home</span><span>Why</span><span>How It Works</span><span>Sign Up</span><span>Our Blog</span></nav>
  </footer>
</div>
</body>
</html>
```